Web Design Project for Lumen Harbor

Design a new web site for Lumen Harbor.

Current design - www.lumenharbor.example
Latest design - store.lumenharbor.example

Close site we like - www.qvr.example

The new design has to be welcoming, fresh, non-industrial, light, friendly and functional.

Target Market(s)

Enterprise IT professionals. In particular, CIO's and IT Managers.

Industry/Entity Type

Store

Requirements
Must have
• Same functionality as the new design.
Should not have
• We want to be able to target different users with different content..... it somethings important to CIO's and not important to Service Delivery Managers, which is different from Network Managers, and different from CFO's.

```html
<!DOCTYPE html>
<html lang="en">
<head>
<meta charset="utf-8">
<title>Lumen Harbor – Next Generation Monitoring Solutions</title>
<link href="https://fonts.googleapis.com/css2?family=Arimo:wght@400;700&family=Lato:wght@400;700;900&display=swap" rel="stylesheet">
<style>
:root{
  --blue-deep:#1c4a7c;
  --blue-mid:#2a64a0;
  --blue-dark:#173e69;
  --blue-title:#1d4f86;
  --green:#2fae3c;
  --green-dark:#1f8a2b;
  --green-soft:#d6f0da;
  --grey-band:#e9e7e3;
  --grey-line:#c9c9c9;
  --text:#4a4a4a;
  --white:#fff;
}
*{box-sizing:border-box;margin:0;padding:0}
html,body{width:1200px;height:1188px;overflow:hidden;background:var(--white);font-family:'Arimo',Arial,sans-serif;color:var(--text)}
.page{position:relative;width:1200px;height:1188px}
.abs{position:absolute}

/* header */
.brand{left:272px;top:38px;display:flex;flex-direction:column}
.brand-row{display:flex;align-items:center;gap:10px}
.brand-mark{width:22px;height:22px;background:var(--blue-title)}
.brand-name{font-family:'Lato',sans-serif;font-weight:900;font-size:28px;color:var(--blue-title);line-height:34px}
.brand-tag{font-size:10px;color:var(--green-dark);font-weight:700;margin-left:32px}
.search{left:705px;top:49px;display:flex}
.search input{width:155px;height:20px;border:1px solid #bbb;border-radius:3px 0 0 3px}
.search button{width:70px;height:22px;background:linear-gradient(#4cc158,var(--green-dark));color:#fff;border:0;border-radius:3px;font-size:10px;font-weight:700;margin-left:-4px}
.nav{left:264px;top:99px;width:675px;height:35px;background:linear-gradient(#fff,#ececec);border:1px solid #d5d5d5;border-radius:3px;display:flex;justify-content:space-around;align-items:center;z-index:2;box-shadow:0 2px 3px rgba(0,0,0,.15)}
.nav a{font-size:9px;letter-spacing:1px;color:#444;text-decoration:none;font-weight:700}
.nav a.active{color:var(--green)}

/* hero */
.hero{left:0;top:125px;width:1200px;height:234px;background:radial-gradient(ellipse at 60% 55%,#3a7ec0 0%,var(--blue-mid) 40%,var(--blue-deep) 100%)}
.hero-title{left:320px;top:196px;font-family:'Lato',sans-serif;color:#e8eef5}
.hero-title h1{font-size:34px;font-weight:900;letter-spacing:1px;line-height:1}
.hero-title p{font-size:20px;font-weight:900;letter-spacing:.5px}
.hero-btn{left:321px;top:293px;width:138px;height:33px;border-radius:8px;background:linear-gradient(#5fd06a,#23992f);border:2px solid #a8e6ad;color:#fff;font-family:'Lato',sans-serif;font-weight:900;font-size:15px;display:flex;align-items:center;justify-content:center;letter-spacing:.5px}
.hero-visual{left:620px;top:168px;width:260px;height:165px;border-radius:10px;background:linear-gradient(135deg,#6b7176,#2c3033 55%,#1b1e20)}
.arrow{width:52px;height:52px}

/* features */
.band{left:0;top:359px;width:1200px;height:241px;background:var(--grey-band)}
.feature{width:330px;height:95px;background:#fff;border:1px solid var(--grey-line);border-top:3px solid #bdbdbd;border-radius:4px;overflow:hidden;box-shadow:0 1px 2px rgba(0,0,0,.1)}
.feature-side{position:absolute;left:0;top:0;width:90px;height:100%;background:linear-gradient(90deg,#eef9f0,var(--green-soft));border-radius:0 60px 60px 0/0 50% 50% 0}
.feature-art{position:absolute;left:16px;top:25px;width:50px;height:36px;border-radius:3px;background:linear-gradient(#3f79b8,#1c4a7c)}
.feature h3{position:absolute;left:104px;top:4px;font-family:'Lato',sans-serif;font-size:12.5px;font-weight:900;color:var(--blue-title)}
.feature p{position:absolute;left:104px;top:22px;width:214px;font-size:8.5px;line-height:10px;color:#777;text-align:justify}
.feature .more{position:absolute;right:10px;bottom:4px;font-size:8.5px;color:#777}

/* industry */
.industry{left:261px;top:610px;width:425px;height:256px;border:1px solid var(--grey-line);border-radius:4px;background:#fff}
.industry h2{position:absolute;left:10px;top:10px;font-family:'Lato',sans-serif;font-size:17px;font-weight:900;color:#333}
.industry .full{position:absolute;right:8px;top:8px;width:90px;height:18px;background:linear-gradient(#2c6aa8,var(--blue-dark));border:1px solid var(--green);color:#fff;font-size:8px;font-weight:700;display:flex;align-items:center;justify-content:center;border-radius:3px}
.industry .rule{position:absolute;left:8px;right:8px;top:34px;border-top:1px solid #ccc}
.industry h4{position:absolute;left:10px;top:40px;font-family:'Lato',sans-serif;font-size:14.5px;font-weight:900;color:#333}
.industry .photo{position:absolute;left:11px;top:64px;width:156px;height:104px;background:linear-gradient(135deg,#d9dde3,#8e98a6 60%,#5c6572)}
.industry .lead{position:absolute;left:176px;top:63px;width:240px;font-size:8px;line-height:13px;letter-spacing:.7px;text-transform:uppercase;color:#333;text-align:justify}
.bullet{position:absolute;left:11px;width:405px;font-size:8px;line-height:13px;letter-spacing:.7px;text-transform:uppercase;color:#333;padding-left:14px}
.bullet::before{content:"";position:absolute;left:0;top:4px;width:5px;height:5px;background:var(--green)}
.dash{position:absolute;left:8px;right:8px;border-top:1px dashed #999}

.solutions{left:696px;top:610px;width:244px;height:256px;border:1px solid var(--grey-line);border-radius:4px;background:#fff}
.solutions h2{position:absolute;left:10px;top:10px;font-family:'Lato',sans-serif;font-size:16px;font-weight:900;color:#333}
.solutions ul{position:absolute;left:10px;top:34px;width:224px;list-style:none}
.solutions li{height:36.5px;border-top:1px dashed #aaa;font-size:8px;font-weight:700;color:var(--blue-dark);display:flex;align-items:center;letter-spacing:.3px}
.solutions li span{margin-left:14px}

/* news */
.news{left:261px;top:871px;width:679px;height:218px;border-radius:4px;background:linear-gradient(#1f5289,#3f7bb7 60%,#5a93c9);border:1px solid #9fb9d4}
.news h2{position:absolute;font-family:'Lato',sans-serif;font-size:15px;font-weight:900;color:#fff;letter-spacing:.3px}
.news .uline{position:absolute;border-top:1px dashed #a9c3dd}
.news-item{position:absolute;width:185px;font-size:11px;line-height:13px;color:#fff;text-transform:uppercase;text-align:justify;letter-spacing:.3px}
.rm{position:absolute;width:74px;height:21px;background:var(--blue-dark);border:1px solid #6f97c0;border-radius:2px;color:#fff;font-size:11px;display:flex;align-items:center;justify-content:center}
.news .divider{position:absolute;left:432px;top:18px;height:190px;border-left:1px dashed #a9c3dd}
.adv{position:absolute;left:444px;top:36px;width:222px;font-size:11px;line-height:15px;color:#eaf1f8;text-align:justify;letter-spacing:.5px}

/* footer */
.footer{left:0;top:1096px;width:1200px;height:92px;background:var(--blue-deep)}
.fnav{left:0;top:1110px;width:1200px;display:flex;justify-content:center;font-size:8.5px;color:#fff;font-weight:700;letter-spacing:.5px}
.fnav span{padding:0 12px;border-right:1px solid #fff}
.fnav span:last-child{border-right:0}
.copy{left:0;top:1132px;width:1200px;text-align:center;font-size:7.5px;color:#d0dcea;letter-spacing:.5px}
.frule{left:261px;top:1152px;width:679px;border-top:1px solid #3e6a98}
.legal{left:0;top:1162px;width:1200px;text-align:center;font-size:8px;color:#d0dcea}
</style>
</head>
<body>
<div class="page">

  <header>
    <div class="abs brand">
      <div class="brand-row"><span class="brand-mark"></span><span class="brand-name">Lumen Harbor</span></div>
      <span class="brand-tag">Next Generation Monitoring Solutions</span>
    </div>
    <form class="abs search"><input type="text" aria-label="Search"><button type="button">Search</button></form>
    <nav class="abs nav">
      <a class="active">HOME</a><a>SOLUTIONS</a><a>TECHNOLOGY</a><a>RESOURCES</a><a>PARTNERS</a><a>COMPANY</a><a>SUPPORT</a><a>CONTACT US</a>
    </nav>
  </header>

  <section class="abs hero"></section>
  <svg class="abs arrow" style="left:240px;top:211px" viewBox="0 0 52 52"><circle cx="26" cy="26" r="25" fill="#1a3f66"/><circle cx="26" cy="26" r="21" fill="#fff"/><path d="M30 16 L20 26 L30 36" fill="none" stroke="#2fae3c" stroke-width="6" stroke-linecap="round" stroke-linejoin="round"/></svg>
  <svg class="abs arrow" style="left:908px;top:211px" viewBox="0 0 52 52"><circle cx="26" cy="26" r="25" fill="#1a3f66"/><circle cx="26" cy="26" r="21" fill="#fff"/><path d="M22 16 L32 26 L22 36" fill="none" stroke="#2fae3c" stroke-width="6" stroke-linecap="round" stroke-linejoin="round"/></svg>
  <div class="abs hero-title"><h1>DISCOVER</h1><p>THE POWER OF EVENTS.</p></div>
  <div class="abs hero-btn">Read More...</div>
  <div class="abs hero-visual" role="img" aria-label="Two tablet computers showing a monitoring dashboard"></div>

  <div class="abs band"></div>
  <article class="abs feature" style="left:261px;top:383px"><div class="feature-side"></div><div class="feature-art" role="img" aria-label="Monitor with bar chart"></div><h3>Lumen Harbor Last Mile Advantage</h3><p>Lumen Harbor can help you solve real world business problems with complex event processing. Gain an understanding of how Lumen Harbor and event processing can help your business.</p><span class="more">» Learn More</span></article>
  <article class="abs feature" style="left:602px;top:383px"><div class="feature-side"></div><div class="feature-art" role="img" aria-label="Monitor with energy dashboard"></div><h3>Desktop Energy Management</h3><p>Lumen Harbor can help you solve real world business problems with complex event processing. Gain an understanding of how Lumen Harbor and event processing can help your business.</p><span class="more">» Learn More</span></article>
  <article class="abs feature" style="left:261px;top:487px"><div class="feature-side"></div><div class="feature-art" role="img" aria-label="Monitor with world map"></div><h3>Lumen Harbor EPN</h3><p>Lumen Harbor can help you solve real world business problems with complex event processing. Gain an understanding of how Lumen Harbor and event processing can help your business.</p><span class="more">» Learn More</span></article>
  <article class="abs feature" style="left:602px;top:487px"><div class="feature-side"></div><div class="feature-art" role="img" aria-label="Monitor with cycle symbol"></div><h3>Event Driven App. Platform</h3><p>Lumen Harbor can help you solve real world business problems with complex event processing. Gain an understanding of how Lumen Harbor and event processing can help your business.</p><span class="more">» Learn More</span></article>

  <section class="abs industry">
    <h2>INDUSTRY LEADING</h2><span class="full">Read full story</span>
    <div class="rule"></div>
    <h4>helping organisations discover the power of events</h4>
    <div class="photo" role="img" aria-label="Man working on a laptop"></div>
    <p class="lead">Lumen Harbor is proud to announce that it is the gold sponsor of the KDX/KDC CIO Summit 2010 Wednesday, April 7, 2010. Lumen Harbor is proud to announce that it is the gold sponsor of the KDX/KDC CIO Summit 2010 Wednesday, April 7, 2010. Announce that it is the gold sponsor of the KDX/KDC CIO Summit 2010 Wednesday, April 7, 2010.</p>
    <p class="bullet" style="top:182px">Announce that it is the gold sponsor of the KDX/KDC CIO Summit 2010 Wednesday, April 7, 2010.</p>
    <div class="dash" style="top:212px"></div>
    <p class="bullet" style="top:218px">Announce that it is the gold sponsor of the KDX/KDC CIO Summit 2010 Wednesday, April 7, 2010.</p>
  </section>

  <section class="abs solutions">
    <h2>Our Solutions</h2>
    <ul>
      <li>Large Scale Vehicle Tracking with ANPR<span>&gt;&gt;</span></li>
      <li>Real Time Asset Condition Monitoring<span>&gt;&gt;</span></li>
      <li>Customer Experience Monitoring<span>&gt;&gt;</span></li>
      <li>Environmental Monitoring<span>&gt;&gt;</span></li>
      <li>Event Driven Application Platform<span>&gt;&gt;</span></li>
      <li>Information and Communication Technology<span>&gt;&gt;</span></li>
    </ul>
  </section>

  <section class="abs news">
    <h2 style="left:18px;top:8px">LATEST NEWS</h2>
    <div class="uline" style="left:12px;top:30px;width:412px"></div>
    <p class="news-item" style="left:18px;top:38px">Lumen Harbor is proud to announce that it is the gold sponsor of the KDX/KDC CIO Summit 2010 Wednesday, April 7, 2010.</p>
    <p class="news-item" style="left:228px;top:38px">Lumen Harbor is proud to announce that it is the gold sponsor of the KDX/KDC CIO Summit 2010 Wednesday, April 7, 2010.</p>
    <span class="rm" style="left:124px;top:106px">Read More</span>
    <span class="rm" style="left:339px;top:106px">Read More</span>
    <p class="news-item" style="left:18px;top:136px">Lumen Harbor is proud to announce that it is the gold sponsor of the KDX/KDC CIO Summit 2010.</p>
    <p class="news-item" style="left:228px;top:136px">Lumen Harbor is proud to announce that it is the gold sponsor of the KDX/KDC CIO Summit 2010.</p>
    <span class="rm" style="left:124px;top:188px">Read More</span>
    <span class="rm" style="left:339px;top:188px">Read More</span>
    <div class="divider"></div>
    <h2 style="left:444px;top:10px">ADVANCED PROGRAM</h2>
    <div class="uline" style="left:440px;top:32px;width:228px"></div>
    <p class="adv">Lumen Harbor offers advanced previews to select customers and industry insiders. To see if you qualify. Lumen Harbor offers advanced previews to select customers and industry insiders. To see if you qualify. Lumen Harbor offers advanced previews to select customers and industry insiders. To see if you qualify.</p>
    <span class="rm" style="left:586px;top:188px">Read More</span>
  </section>

  <footer>
    <div class="abs footer"></div>
    <nav class="abs fnav"><span>HOME</span><span>THE ORGANIZATION</span><span>OUR OPERATIONS</span><span>NEWS &amp; EVENTS</span><span>SPONSORS</span><span>COMMUNITY</span><span>BLOG</span><span>CONTACT US</span></nav>
    <p class="abs copy">Copyright 2012. All Rights Are Reserved. LUMENHARBOR.EXAMPLE</p>
    <div class="abs frule"></div>
    <p class="abs legal">Terms of Services | Privacy Policy</p>
  </footer>

</div>
</body>
</html>
```